7KT Guided Signal: Welfare - A book about Welfare Messaging

Please refer to sample covers in the attached files none of which I found adequate.I would prefer a book cover that some kind of construction photo with people in it.
Book size is 6"*9"
“7KT Guided Signal: Welfare” is a short book that is intended to provide some background and explanation in support of the 7KT Welfare.com work site. The book is set up on Brindlemart.com’s pagelume site.
I would like to display the 7KT Welfare logo, title, author name on the front cover with a suitable construction oriented photo in support of that. On the back cover I’d like to show if it makes sense the essence of 7KT Welfare.com which is as follows:
7KT:
Right Messages,
Right People,
Right Time,
Right results
Prioritized
Proactive
Painless
Patented
7KT builds on the analysis of any process, near miss, accident, or incident and the subsequent repackaging of the resultant messages for delivery, audit and follow up on an ongoing basis. The messages and follow up are relentless and delivered before any subsequent events can occur. Specific and detailed messages from are managed; they are not forgotten. Quality is checked on a continuous basis.
A Welfare Culture consists of the pool of ideas, thoughts, images, practices, written text, and beliefs that all constitute messages and guide our actions in the workplace. 7KT is designed to support existing practices and replace some of the less effective practices.
7KT simplifies the transmission of safety messages, information and ideas. Single messages will be easily handled and not lost in the sea of competing messages.
In its most simple form, a message is an idea a person either receives, or conceives and can communicate to another person. Messages include training, posters, hardhat stickers, safety manuals.
Updates
I would like to consider the following bylines for inclusion somewhere on the front or back cover of the book.Note that the book cover is designed to be used on PrintNook and so the cover will include the front and back of the book."The New Standard For Welfare Messages Building a Culture of Confidence" Added Thursday, May 28, 2015
Target Market(s)
Welfare Professionals worldwide
Industry/Entity Type
Construction
Requirements
Must have
- A back cover and be set up for Print Nook,
- The Title of the Book is 7KT Guided Signal: Welfare
Nice to have
- A color construction Photo that spans back and front covers and comforms to the theme of the book.
- Tag lines that include:
- The New Standard in Welfare Messaging
- Building a Culture of Confidence

```html
<!DOCTYPE html>
<html lang="en">
<head>
<meta charset="utf-8">
<title>7KT Guided Signal: Welfare — Cover</title>
<link rel="stylesheet" href="https://fonts.googleapis.com/css2?family=Archivo+Black&family=Anton&family=Arimo:ital,wght@0,700;1,700&family=Cinzel:wght@600&display=swap">
<style>
  :root {
    --yellow: #ffe600;
    --yellow-deep: #f3d600;
    --black: #111111;
    --red: #c8102e;
    --bright-red: #ee1c25;
    --navy: #2b3a67;
    --slate: #6f7f96;
    --ink: #1a1a1a;
  }
  * { box-sizing: border-box; margin: 0; padding: 0; }
  html, body { width: 1200px; height: 868px; overflow: hidden; background: var(--yellow); }
  .cover {
    position: relative; width: 1200px; height: 868px; overflow: hidden;
    background: var(--yellow);
    font-family: "Arimo", Arial, sans-serif; color: var(--ink);
  }
  .hazard {
    position: absolute; height: 32px;
    background: repeating-linear-gradient(60deg, var(--black) 0 18px, transparent 18px 44px);
  }
  .hazard--top { left: 0; top: 37px; width: 595px; }
  .hazard--bottom { left: 0; top: 773px; width: 1200px; height: 40px; }

  .back-photo {
    position: absolute; left: 0; top: 0; width: 600px; height: 868px;
    background: radial-gradient(ellipse at 25% 40%, rgba(190,170,60,.35), rgba(255,230,0,0) 65%),
                linear-gradient(180deg, rgba(220,200,40,.25), rgba(255,230,0,0) 70%);
  }
  .back-mark {
    position: absolute; left: 0; width: 590px; top: 118px; text-align: center;
    font-family: "Archivo Black", sans-serif; font-size: 50px; letter-spacing: 1px; color: var(--black);
  }
  .essence {
    position: absolute; top: 216px; font-weight: 700; font-size: 18px; line-height: 24px; color: var(--black);
  }
  .essence--right { left: 57px; }
  .essence--p { left: 400px; }
  .essence em { font-style: normal; color: var(--red); }
  .badge {
    position: absolute; left: 240px; top: 178px; width: 92px; height: 92px;
    display: flex; align-items: center; justify-content: center; flex-direction: column;
  }
  .badge__dot { width: 58px; height: 58px; border-radius: 50%; background: var(--red); }
  .badge__name { margin-top: 4px; font-weight: 700; font-size: 12px; color: var(--red); white-space: nowrap; }

  .proven {
    position: absolute; left: 0; width: 570px; top: 332px; text-align: center;
    font-weight: 700; font-size: 14px;
  }
  .proven b, .blurb b { color: var(--red); }
  .blurb {
    position: absolute; left: 57px; width: 540px; font-weight: 700; font-size: 13px; line-height: 22px;
  }
  .blurb i { font-style: italic; }
  .blurb--1 { top: 367px; }
  .blurb--2 { top: 498px; }
  .blurb--3 { top: 563px; }
  .blurb--4 { top: 629px; }

  .front-mark {
    position: absolute; left: 655px; top: 20px; width: 500px; text-align: center;
    font-family: "Archivo Black", sans-serif; font-size: 168px; line-height: 190px; letter-spacing: -4px;
    color: var(--slate);
    -webkit-text-stroke: 4px var(--black);
  }
  .tagline {
    position: absolute; left: 615px; width: 580px; top: 200px; text-align: center;
    font-weight: 700; font-size: 17.5px; letter-spacing: .3px; color: var(--red);
  }
  .title {
    position: absolute; left: 615px; width: 580px; top: 215px; text-align: center;
    font-family: "Anton", sans-serif; font-size: 60px; line-height: 70px; color: var(--navy);
    letter-spacing: .5px;
  }
  .title-word {
    position: absolute; left: 615px; width: 580px; top: 278px; text-align: center;
    font-family: "Archivo Black", sans-serif; font-size: 92px; line-height: 100px; color: var(--bright-red);
    -webkit-text-stroke: 2px var(--black); letter-spacing: 2px;
  }
  .front-photo {
    position: absolute; left: 640px; top: 360px; width: 560px; height: 413px;
    background: linear-gradient(180deg, rgba(240,240,240,.55) 0 18%, rgba(38,52,98,.9) 32%, #1f2b55 100%);
    border-radius: 200px 160px 0 0;
  }
  .author {
    position: absolute; left: 640px; width: 540px; top: 832px; text-align: center;
    font-family: "Cinzel", serif; font-size: 22px; letter-spacing: 2px; color: var(--ink);
  }
</style>
</head>
<body>
<main class="cover">
  <div class="back-photo" role="img" aria-label="Faint construction site with an excavator and building blocks"></div>
  <div class="hazard hazard--top"></div>

  <section class="back">
    <div class="back-mark">7KT</div>
    <div class="essence essence--right">
      <em>Right</em> Messages,<br><em>Right</em> People,<br><em>Right</em> Time,<br><em>Right</em> results
    </div>
    <div class="badge"><span class="badge__dot"></span><span class="badge__name">7KT Welfare</span></div>
    <div class="essence essence--p">
      <em>P</em>rioritized<br><em>P</em>roactive<br><em>P</em>ainless<br><em>P</em>atented
    </div>
    <p class="proven"><b>7KT</b> - a proven and patented messaging system.</p>
    <p class="blurb blurb--1">The consistent use of <b>7KT</b> results in an engaged, educated, safe and confident workforce. <i>It can be applied to any business.</i><br>A successful Safety Culture is a culture of confidence. It consists of a pool of ideas, thoughts, images, practices and approaches to safety that are consistent and work together, to deliver a safe workplace.</p>
    <p class="blurb blurb--2"><b>7KT</b> simplifies the transmission of safety messages, boosts communication. Specific messages are prioritized, repeated and not forgotten. Single messages will be easily handled and not lost in the sea of conflicting messages.</p>
    <p class="blurb blurb--3"><b>7KT</b> supports existing communication practices such as cell phones and email and in many cases replaces some of the less effective communications to employees.</p>
    <p class="blurb blurb--4"><b>7KT</b> communicates directly to the workforce every day, in Clear, Concise, Memorable messages to enhance a Safety Culture of Confidence.</p>
  </section>

  <section class="front">
    <div class="front-mark">7KT</div>
    <p class="tagline">THE NEW STANDARD IN SAFETY MESSAGING</p>
    <h1 class="title">GUIDED SIGNAL:</h1>
    <p class="title-word">WELFARE</p>
    <div class="front-photo" role="img" aria-label="Two site workers in navy overalls, hard hats and ear defenders reviewing a folding ruler"></div>
    <p class="author">MARCUS T. OBERLIN P.ENG</p>
  </section>

  <div class="hazard hazard--bottom"></div>
</main>
</body>
</html>
```